A small boutique Accounting and Mortgage Broking firm needs a business card design

Torvel is a Brisbane based boutique accounting and mortgage broking firm. We offer a range of extensive financial services like accounting, tax consulting, book-keeping and mortgage broking.
We need a business card that stands out. The content can stay as it is on the existing card unless you recommend us to change anything on it for a better design.
Please remove the mobile number and give us a suitable format to change the details like email address and name.
Contact Information for Business Card
Dilan Karodi
Torvel Group Pty Ltd
3/412 Wendle Rd Kellbrook QLD 4219
PO Box 829 Kellbrook QLD 4219
T 07 3184 5526
F 07 3952 1873
E dkarodi@torvel-example.net.au
Accountants Tax Agents, Mortgage Brokers
www.torvel-example.net.au

```html
<!DOCTYPE html>
<html lang="en">
<head>
<meta charset="utf-8">
<title>Torvel – Business Card</title>
<link rel="stylesheet" href="https://fonts.googleapis.com/css2?family=Montserrat:wght@300;700&family=Oswald:wght@400;500&display=swap">
<style>
  :root {
    --green: #7cc242;
    --green-light: #8fd150;
    --green-deep: #5fa62e;
    --charcoal: #3b3b3d;
    --paper: #ffffff;
    --backdrop: #e8e5e0;
  }
  * { box-sizing: border-box; margin: 0; padding: 0; }
  html, body { width: 1200px; height: 1200px; overflow: hidden; }
  body { background: var(--backdrop); position: relative; }

  .card {
    position: absolute;
    left: 150px;
    width: 900px;
    height: 514px;
    overflow: hidden;
    box-shadow: 0 10px 30px rgba(0,0,0,.18);
  }

  /* Front */
  .card--front {
    top: 70px;
    background: radial-gradient(ellipse at 50% 40%, var(--green-light), var(--green) 55%, var(--green-deep));
  }
  .brand {
    position: absolute;
    left: 0; right: 0; top: 118px;
    display: flex; justify-content: center; align-items: center; gap: 26px;
  }
  .brand__circle {
    width: 96px; height: 96px; border-radius: 50%;
    border: 14px solid var(--charcoal);
  }
  .brand__name {
    font-family: "Montserrat", sans-serif;
    font-weight: 700; font-size: 112px; line-height: 1;
    color: var(--charcoal); letter-spacing: -2px;
  }
  .tagline {
    position: absolute; left: 0; right: 0; top: 262px; text-align: center;
    font-family: "Montserrat", sans-serif; font-weight: 300;
    font-size: 40px; letter-spacing: 3px; color: var(--charcoal);
  }
  .services {
    position: absolute; left: 0; right: 0; top: 346px; text-align: center;
    font-family: "Oswald", sans-serif; font-weight: 500;
    font-size: 27px; letter-spacing: 2.5px; color: var(--charcoal);
  }
  .website {
    position: absolute; left: 0; right: 0; top: 412px; text-align: center;
    font-family: "Oswald", sans-serif; font-weight: 500;
    font-size: 24px; letter-spacing: 3px; color: var(--paper);
  }

  /* Back */
  .card--back { top: 630px; background: var(--paper); }
  .card__swoosh { position: absolute; inset: 0; width: 100%; height: 100%; }
  .mark {
    position: absolute; left: 60px; top: 222px;
    display: flex; align-items: center; gap: 14px;
  }
  .mark__circle {
    width: 58px; height: 58px; border-radius: 50%;
    border: 10px solid var(--charcoal);
  }
  .mark__name {
    font-family: "Montserrat", sans-serif; font-weight: 700;
    font-size: 58px; line-height: 1; color: var(--charcoal); letter-spacing: -1px;
  }
  .divider {
    position: absolute; left: 388px; top: 150px;
    width: 3px; height: 240px; background: var(--green);
  }
  .contact {
    position: absolute; left: 420px; top: 150px;
    font-family: "Oswald", sans-serif; color: var(--charcoal);
  }
  .contact__name { font-size: 40px; font-weight: 500; letter-spacing: 1.5px; line-height: 1.1; margin-bottom: 10px; }
  .contact__list { list-style: none; }
  .contact__item {
    display: flex; align-items: center; gap: 14px;
    font-size: 22px; letter-spacing: 1px; line-height: 38px;
  }
  .contact__icon { width: 20px; height: 20px; flex: none; fill: var(--green); }
</style>
</head>
<body>

<section class="card card--front" aria-label="Business card front">
  <div class="brand">
    <span class="brand__circle"></span>
    <span class="brand__name">Torvel</span>
  </div>
  <p class="tagline">CLARITY. CARE. PROGRESS.</p>
  <p class="services">ACCOUNTANTS TAX AGENTS | BOOK-KEEPER | MORTGAGE BROKERS</p>
  <p class="website">www.torvel-example.net.au</p>
</section>

<section class="card card--back" aria-label="Business card back">
  <svg class="card__swoosh" viewBox="0 0 900 514" preserveAspectRatio="none" aria-hidden="true">
    <path d="M0 0 H900 V150 C720 70 420 40 0 60 Z" fill="var(--green)"/>
    <path d="M560 0 H900 V120 C820 70 700 30 560 0 Z" fill="var(--charcoal)"/>
    <path d="M0 70 C420 40 700 60 900 165 V514 H0 Z" fill="var(--paper)"/>
    <path d="M0 420 C130 432 260 466 380 514 H0 Z" fill="var(--charcoal)"/>
    <path d="M0 448 C110 456 220 480 300 514 H0 Z" fill="var(--green)"/>
    <path d="M0 420 C130 432 260 466 380 514 H360 C250 476 130 446 0 436 Z" fill="var(--charcoal)"/>
  </svg>

  <div class="mark">
    <span class="mark__circle"></span>
    <span class="mark__name">Torvel</span>
  </div>

  <div class="divider"></div>

  <div class="contact">
    <p class="contact__name">Dilan Karodi</p>
    <ul class="contact__list">
      <li class="contact__item">
        <svg class="contact__icon" viewBox="0 0 20 20"><path d="M10 1a6.5 6.5 0 0 0-6.5 6.5C3.5 12.5 10 19 10 19s6.5-6.5 6.5-11.5A6.5 6.5 0 0 0 10 1zm0 9a2.5 2.5 0 1 1 0-5 2.5 2.5 0 0 1 0 5z"/></svg>
        3/412 Wendle Rd Kellbrook QLD 4219
      </li>
      <li class="contact__item">
        <svg class="contact__icon" viewBox="0 0 20 20"><path d="M10 1a6.5 6.5 0 0 0-6.5 6.5C3.5 12.5 10 19 10 19s6.5-6.5 6.5-11.5A6.5 6.5 0 0 0 10 1zm0 9a2.5 2.5 0 1 1 0-5 2.5 2.5 0 0 1 0 5z"/></svg>
        PO Box 829 Kellbrook QLD 4219
      </li>
      <li class="contact__item">
        <svg class="contact__icon" viewBox="0 0 20 20"><path d="M1 7c0-2 4-4 9-4s9 2 9 4v2h-4V7H5v2H1zM4 10h12l2 7H2z"/></svg>
        07 3184 5526
      </li>
      <li class="contact__item">
        <svg class="contact__icon" viewBox="0 0 20 20"><path d="M5 2h8l2 2v4H5zM2 9h16v9H2zm3 3v2h4v-2z"/></svg>
        07 3952 1873
      </li>
      <li class="contact__item">
        <svg class="contact__icon" viewBox="0 0 20 20"><path d="M1 4h18v12H1zm1.5 1.5L10 11l7.5-5.5z"/></svg>
        dkarodi@torvel-example.net.au
      </li>
    </ul>
  </div>
</section>

</body>
</html>
```